KV Group

We need a new website for our company and since we had a very good work done for our logo in this site, we're back for the entire job.

Our company name is Marlowe Capital Group. We're adding files of examples of what we have done today. In my opinion we need a more attention lock in the site but yet financial simple work.

Our files (attached) will let you know what we have so far. We need a complete change but the colours should be the same, however you can change them not running away to far from the original, and of course matching with the logo.

We need examples for 3 kind of layouts.

- A HOME welcome layout
- An internal Layout with sidebar
- And internal Layout wide

We can buy image licenses if needed for assets.
Actually there are 5 slide images placed on the Welcome HOME, we need those there, but you can improve with better images to match the new website!!!

Target Market(s)

Clients looking for financial advisers, tax and funds specialist, currency advisers

Industry/Entity Type

Financial

Requirements
Must have
• all the fonts must be in accordance with the financial market sites........the welcome home page must be precise, neat and information accurate........the menu should be elegant........main focus on the Home page, should be also the PRIVATE ACCESS box log in.......

```html
<!DOCTYPE html>
<html lang="en">
<head>
<meta charset="utf-8">
<title>Marlowe Capital Group – Home Slides</title>
<link href="https://fonts.googleapis.com/css2?family=Yanone+Kaffeesatz:wght@400;500&family=Arimo:wght@400;700&display=swap" rel="stylesheet">
<style>
  :root {
    --orange: #f47c20;
    --orange-deep: #e2660f;
    --title-orange: #f7861e;
    --highlight: #f8b27f;
    --caption-bg: rgba(22, 22, 22, 0.84);
    --caption-fold: #111111;
    --field-bg: #f1efec;
    --field-text: #a9a6a2;
    --button-bg: #1a1a1a;
    --white: #ffffff;
    --dot-border: #333333;
  }
  * { box-sizing: border-box; margin: 0; padding: 0; }
  html, body {
    width: 1200px; height: 739px; overflow: hidden;
    background: var(--white);
  }
  .stage {
    width: 1100px; height: 677.4px;
    transform: scale(1.0909); transform-origin: 0 0;
    position: relative;
  }
  .hero { position: absolute; left: 67px; width: 960px; height: 312px; }
  .hero--services { top: 10px; }
  .hero--investments { top: 331px; }

  .slide-visual {
    position: absolute; left: 10px; top: 0; width: 696px; height: 286px;
  }
  .slide-visual--services {
    background: linear-gradient(135deg, #f6d77a 0%, #d9a43a 35%, #f3d98b 60%, #a86f18 100%);
  }
  .slide-visual--investments {
    background: linear-gradient(160deg, #f3f3f1 0%, #dfe0dc 45%, #cfd6a0 75%, #b8cf4a 100%);
  }

  .caption {
    position: absolute; left: 0; top: 130px; width: 624px; height: 103px;
    background: var(--caption-bg);
    padding: 6px 24px 0 24px;
    font-family: "Yanone Kaffeesatz", sans-serif;
  }
  .caption::after {
    content: ""; position: absolute; left: 0; bottom: -9px;
    border-top: 9px solid var(--caption-fold); border-left: 10px solid transparent;
  }
  .caption__title {
    color: var(--title-orange); font-size: 29px; font-weight: 400; line-height: 34px;
  }
  .caption__text {
    color: var(--white); font-size: 21px; font-weight: 400; line-height: 23px; margin-top: 4px;
  }
  .caption__text em { font-style: normal; color: var(--highlight); }

  .pager {
    position: absolute; left: 646px; top: 296px; display: flex; gap: 3px;
  }
  .pager__dot {
    width: 10px; height: 10px; border-radius: 50%;
    border: 1px solid var(--dot-border); background: var(--white);
  }
  .pager__dot--active { background: var(--orange); }

  .access {
    position: absolute; left: 713px; top: 0; width: 237px; height: 286px;
    background: var(--orange); overflow: hidden;
  }
  .access__art {
    position: absolute; left: 120px; top: 140px; width: 130px; height: 140px;
    background: radial-gradient(ellipse at 45% 50%, rgba(200, 90, 20, 0.55) 0%, rgba(244, 124, 32, 0) 70%);
  }
  .access__title {
    position: absolute; left: 10px; top: 14px;
    font-family: "Yanone Kaffeesatz", sans-serif; font-size: 29px; color: var(--white); font-weight: 400;
  }
  .access__icon { position: absolute; left: 147px; top: 8px; }
  .access__field {
    position: absolute; left: 9px; width: 219px; height: 30px;
    background: var(--field-bg); border: none; padding-left: 8px;
    font-family: "Arimo", sans-serif; font-size: 12px; font-weight: 700; color: var(--field-text);
    display: flex; align-items: center;
  }
  .access__field--number { top: 75px; }
  .access__field--password { top: 114px; }
  .access__forgot {
    position: absolute; left: 10px; top: 155px;
    font-family: "Arimo", sans-serif; font-size: 11.5px; color: var(--white);
  }
  .access__login {
    position: absolute; left: 9px; top: 203px; width: 96px; height: 30px;
    background: var(--button-bg); color: var(--white); border: none;
    font-family: "Arimo", sans-serif; font-size: 12px;
    box-shadow: 2px 2px 4px rgba(0, 0, 0, 0.35);
    display: flex; align-items: center; justify-content: center;
  }
</style>
</head>
<body>
<main class="stage">

  <section class="hero hero--services">
    <div class="slide-visual slide-visual--services" role="img" aria-label="Golden 3D dollar signs over a calendar grid"></div>
    <div class="caption">
      <h2 class="caption__title">Online Services</h2>
      <p class="caption__text">Manage your everyday finances easily with eBanking. <em>Online Services</em> are available,<br>whenever it is most convenient.</p>
    </div>
    <div class="pager">
      <span class="pager__dot"></span><span class="pager__dot"></span><span class="pager__dot"></span><span class="pager__dot pager__dot--active"></span><span class="pager__dot"></span>
    </div>
    <aside class="access">
      <div class="access__art" role="img" aria-label="Key in a puzzle piece illustration"></div>
      <h3 class="access__title">Private Access</h3>
      <svg class="access__icon" width="50" height="50" viewBox="0 0 50 50" aria-hidden="true">
        <circle cx="25" cy="25" r="24" fill="#f9a15c" stroke="#fff" stroke-width="2"/>
        <circle cx="25" cy="25" r="18" fill="#f47c20" stroke="#fde0c6" stroke-width="1.5"/>
        <circle cx="25" cy="20" r="5.5" fill="#fff"/>
        <path d="M14 35 Q25 22 36 35 Z" fill="#fff"/>
      </svg>
      <div class="access__field access__field--number">Acc. Number</div>
      <div class="access__field access__field--password">Acc. password</div>
      <p class="access__forgot">Forget Password?</p>
      <div class="access__login">LOGIN</div>
    </aside>
  </section>

  <section class="hero hero--investments">
    <div class="slide-visual slide-visual--investments" role="img" aria-label="Hands with pen and calculator over printed bar charts"></div>
    <div class="caption">
      <h2 class="caption__title">Investements</h2>
      <p class="caption__text">We'll help you manage your cash resources effectively <em>increasing profitability</em> while<br>maintaining good liquidity.</p>
    </div>
    <div class="pager">
      <span class="pager__dot"></span><span class="pager__dot"></span><span class="pager__dot"></span><span class="pager__dot"></span><span class="pager__dot pager__dot--active"></span>
    </div>
    <aside class="access">
      <div class="access__art" role="img" aria-label="Key in a puzzle piece illustration"></div>
      <h3 class="access__title">Private Access</h3>
      <svg class="access__icon" width="50" height="50" viewBox="0 0 50 50" aria-hidden="true">
        <circle cx="25" cy="25" r="24" fill="#f9a15c" stroke="#fff" stroke-width="2"/>
        <circle cx="25" cy="25" r="18" fill="#f47c20" stroke="#fde0c6" stroke-width="1.5"/>
        <circle cx="25" cy="20" r="5.5" fill="#fff"/>
        <path d="M14 35 Q25 22 36 35 Z" fill="#fff"/>
      </svg>
      <div class="access__field access__field--number">Acc. Number</div>
      <div class="access__field access__field--password">Acc. password</div>
      <p class="access__forgot">Forget Password?</p>
      <div class="access__login">LOGIN</div>
    </aside>
  </section>

</main>
</body>
</html>
```